Maple Hollow Bloom Backdrops Business card

Looking to have a business card design incorporating my logo for my flower wall business.

Industry/Entity Type

Wedding & event planning

Contact Information for Business Card

My business logo, my name - Jill Worthing (owner), my tagline - Let us be your something extra, phone # 401-627-3918, email address - maplehollowbloombackdrops@fernpost.com, my website - maplehollowbloombackdrops.com, Instagram handle- @maplehollowbloombackdrops, FB handle Handle - maplehollowbloombackdrops

Font styles to use
Other font styles liked:
• Sentaina is the font that is used in my logo

Requirements
Must have
• Would like a double sided business card

```html
<!DOCTYPE html>
<html lang="en">
<head>
<meta charset="utf-8">
<title>Maple Hollow Bloom Backdrops – Business Card</title>
<link rel="stylesheet" href="https://fonts.googleapis.com/css2?family=Poppins:wght@400;500;600;700&family=Kaushan+Script&display=swap">
<style>
  :root {
    --stage: #cbcbcb;
    --blush: #f2dbe8;
    --magenta: #c8287f;
    --ink: #262626;
    --white: #ffffff;
    --gold-light: #f3d27a;
    --gold-dark: #c7953e;
  }
  * { box-sizing: border-box; margin: 0; padding: 0; }
  html, body {
    width: 1200px; height: 1064px; overflow: hidden;
    background: var(--stage);
    font-family: "Poppins", sans-serif;
  }
  .canvas { position: relative; width: 1200px; height: 1064px; }
  .card {
    position: absolute; top: 110px; width: 446px; height: 775px;
    border-radius: 28px; overflow: hidden;
  }
  .card--front { left: 140px; background: var(--blush); }
  .card--back { left: 656px; background: var(--magenta); }

  .brand-seal {
    position: absolute; left: 66px; top: 66px; width: 314px; height: 314px;
    border-radius: 50%; background: var(--white);
    display: flex; align-items: center; justify-content: center; text-align: center;
    padding: 40px;
    font-weight: 500; font-size: 27px; line-height: 1.25; color: var(--magenta);
  }

  .owner-name {
    position: absolute; left: 0; right: 0; top: 400px; text-align: center;
    font-weight: 600; font-size: 39px; line-height: 58px; color: var(--ink); letter-spacing: 0.2px;
  }
  .owner-role {
    position: absolute; left: 0; right: 0; top: 447px; text-align: center;
    font-weight: 600; font-size: 19px; line-height: 28px; color: var(--magenta);
  }

  .divider { position: absolute; top: 501px; height: 2px; }
  .divider--left { left: 29px; width: 140px; background: linear-gradient(90deg, transparent, var(--gold-dark)); }
  .divider--right { left: 277px; width: 140px; background: linear-gradient(90deg, var(--gold-dark), transparent); }
  .contact-icon {
    position: absolute; top: 486px; width: 32px; height: 32px;
    border-radius: 8px; background: var(--magenta);
  }
  .contact-icon svg { display: block; width: 32px; height: 32px; }
  .contact-icon--mail { left: 184px; }
  .contact-icon--web { left: 228px; }

  .contact-line {
    position: absolute; left: 0; right: 0; text-align: center;
    font-size: 16.5px; line-height: 26px; color: var(--ink);
  }
  .contact-line--email { top: 522px; }
  .contact-line--web { top: 551px; }

  .find-us {
    position: absolute; left: 32px; top: 607px;
    font-size: 21px; line-height: 32px; color: var(--magenta);
  }
  .social {
    position: absolute; left: 125px; display: flex; align-items: center; gap: 9px;
    font-size: 16px; line-height: 31px; color: var(--magenta); white-space: nowrap;
  }
  .social--instagram { top: 606px; }
  .social--facebook { top: 643px; }
  .social__dot {
    width: 31px; height: 31px; border-radius: 50%;
    border: 2.5px solid var(--magenta); flex: none;
  }

  .phone-band { position: absolute; left: 0; bottom: 0; width: 446px; height: 95px; }
  .phone-band svg { display: block; }
  .phone {
    position: absolute; left: 25px; bottom: 18px; display: flex; align-items: center; gap: 8px;
    color: var(--white); font-size: 40px; font-weight: 400;
  }
  .phone svg { width: 48px; height: 48px; }

  .tagline {
    position: absolute; left: 0; top: 334px; width: 446px;
    font-family: "Kaushan Script", cursive; font-size: 46px; line-height: 1.4;
    background: linear-gradient(180deg, var(--gold-light), var(--gold-dark));
    -webkit-background-clip: text; background-clip: text; color: transparent;
  }
  .tagline span { display: block; white-space: nowrap; }
  .tagline__first { padding-left: 50px; }
  .tagline__second { padding-left: 100px; }
</style>
</head>
<body>
<main class="canvas">
  <section class="card card--front" aria-label="Card front">
    <div class="brand-seal">Maple Hollow Bloom Backdrops</div>

    <h1 class="owner-name">Jill Worthing</h1>
    <p class="owner-role">Owner</p>

    <span class="divider divider--left"></span>
    <span class="divider divider--right"></span>
    <span class="contact-icon contact-icon--mail">
      <svg viewBox="0 0 32 32"><rect x="8" y="10" width="16" height="12" rx="1.5" fill="none" stroke="#fff" stroke-width="1.8"/><path d="M8.5 11 16 17l7.5-6" fill="none" stroke="#fff" stroke-width="1.8"/></svg>
    </span>
    <span class="contact-icon contact-icon--web">
      <svg viewBox="0 0 32 32"><circle cx="14.5" cy="14.5" r="5.5" fill="none" stroke="#fff" stroke-width="2"/><path d="m18.5 18.5 5 5" stroke="#fff" stroke-width="2.4" stroke-linecap="round"/></svg>
    </span>

    <p class="contact-line contact-line--email">maplehollowbloombackdrops@fernpost.com</p>
    <p class="contact-line contact-line--web">maplehollowbloombackdrops.com</p>

    <p class="find-us">Find Us</p>
    <div class="social social--instagram"><span class="social__dot"></span>@maplehollowbloombackdrops</div>
    <div class="social social--facebook"><span class="social__dot"></span>maplehollowbloombackdrops</div>

    <div class="phone-band">
      <svg width="446" height="95" viewBox="0 0 446 95"><path d="M0 14 Q223 -8 446 14 V95 H0 Z" fill="var(--magenta)"/></svg>
    </div>
    <div class="phone">
      <svg viewBox="0 0 48 48"><circle cx="24" cy="24" r="21" fill="none" stroke="#fff" stroke-width="3"/><path d="M17 13.5c1-.8 2.3-.6 3 .4l2.3 3.4c.6.9.4 2-.4 2.7l-1.6 1.3c1.2 2.6 3.2 4.7 5.8 6l1.3-1.6c.7-.8 1.9-1 2.7-.4l3.4 2.3c1 .7 1.2 2 .4 3l-1.5 1.8c-1 1.2-2.6 1.6-4 1-6.6-2.6-11.6-7.6-14.2-14.2-.5-1.4-.1-3 1-4z" fill="#fff"/></svg>
      <span>401-627-3918</span>
    </div>
  </section>

  <section class="card card--back" aria-label="Card back">
    <p class="tagline">
      <span class="tagline__first">Let us be your</span>
      <span class="tagline__second">something extra</span>
    </p>
  </section>
</main>
</body>
</html>
```